PSD website for property company

Please read the brief thoroughly.

We are looking for a new website for a property group that does property acquisitions, property development and property management.
They buy, build and lease core inner city industrial assets in Sydney, Australia.
They also invest in residential developments.

Site menu
- Home page
- Property – sub menus include – Leasing ; Projects ; Investments ; Property Management
- Capital and finance
- About
- Contact

They like this website
https://www.verlo.com.au/

They want the site to be clean, modern and bold.
They like few colors, even black and white is OK to submit

They have a logo and style guide and useable images here:
http://www.kumet.net/temp/PelorisWeb2019.zip
The zip file is also attached to this project.
We have supplied some images to give you an idea, but we will also require you to provide at least 3 extra images from stock photos.
Use your imagination.

I am expecting a lot of similar designs, so be aware the photos you choose will be really important.
They want really 3 good stock photos used and supplied without charge.
Please not too generic, I repeat the quality of the photos is important.
You may provide several photos (but not in multiple submissions please) and we will choose the best three to be provided.

The winner will be selected on a single home page design and required to provide;
All photos use in original format without charge
A second ‘standard page’ template design based on the winning home page design

```html
<!DOCTYPE html>
<html lang="en">
<head>
<meta charset="utf-8">
<title>Peloris – Property Group</title>
<link href="https://fonts.googleapis.com/css2?family=Montserrat:wght@500;600;700;800;900&family=Arimo:wght@400;700&display=swap" rel="stylesheet">
<style>
:root{
  --green:#3d5c22;
  --green-dark:#34501c;
  --mint:#eaf2e1;
  --footer:#86a07e;
  --ink:#222222;
  --body:#3a3a3a;
  --white:#ffffff;
}
*{margin:0;padding:0;box-sizing:border-box}
html,body{width:1200px;height:3708px;overflow:hidden}
body{position:relative;background:var(--white);font-family:Arimo,Arial,sans-serif;color:var(--body)}
.abs{position:absolute}
.photo{position:absolute}

/* hero */
.hero{left:0;top:0;width:1200px;height:680px;
  background:linear-gradient(180deg,#7d8a9a 0%,#a7b1bb 22%,#8c8c86 45%,#5f6a4a 70%,#3f4a34 100%)}
.hero-shade{left:0;top:0;width:1200px;height:680px;background:rgba(20,28,40,.32)}
.nav a{position:absolute;top:84px;font-family:Montserrat,sans-serif;font-weight:600;font-size:13px;letter-spacing:.5px;color:var(--white);text-decoration:none}
.nav .active{left:75px;top:68px;width:62px;height:47px;background:var(--green);display:flex;align-items:center;justify-content:center}
.brand{left:450px;top:62px;width:300px;text-align:center;font-family:Montserrat,sans-serif;font-weight:600;font-size:56px;letter-spacing:16px;color:var(--white);line-height:60px}
.social-top{left:998px;top:84px;display:flex;gap:12px}
.social-top span{width:12px;height:12px;border-radius:50%;background:var(--white)}
.hero-title{left:0;top:245px;width:1200px;text-align:center;font-family:Montserrat,sans-serif;font-weight:900;font-size:104px;letter-spacing:2px;color:var(--white);line-height:110px}
.hero-sub{left:200px;top:350px;width:800px;text-align:center;font-family:Arimo,sans-serif;font-weight:700;font-size:30px;line-height:40px;color:var(--white);letter-spacing:.5px}
.dots{left:551px;top:617px;display:flex;gap:14px}
.dots span{width:13px;height:13px;border-radius:50%;background:#1f2a3b}
.dots span.on{background:var(--white)}

/* intro */
.intro{left:150px;top:730px;width:900px;text-align:center;color:var(--green);font-size:21px;line-height:36px}

/* property */
.property{left:0;top:888px;width:1200px;height:1098px;background:var(--mint)}
.section-title{font-family:Montserrat,sans-serif;font-weight:900;font-size:38px;letter-spacing:1px;color:var(--ink)}
.property .section-title{position:absolute;left:0;top:50px;width:1200px;text-align:center}
.card-photo{width:513px;height:269px}
.card{width:439px;height:204px;background:var(--white);padding:26px 26px 0 26px}
.card h3{font-family:Montserrat,sans-serif;font-weight:700;font-size:22px;color:var(--ink);letter-spacing:.5px;margin-bottom:10px}
.card p{font-size:14px;line-height:29px;color:var(--body)}
.card a{display:block;margin-top:8px;font-family:Montserrat,sans-serif;font-weight:700;font-size:14px;color:var(--green);text-decoration:none;letter-spacing:.3px}

/* split sections */
.split h2{margin-bottom:18px}
.split p{font-size:14.5px;line-height:28.5px;color:var(--body)}
.btn{display:inline-flex;align-items:center;justify-content:center;width:204px;height:54px;background:var(--green);color:var(--white);font-family:Montserrat,sans-serif;font-weight:700;font-size:18px;letter-spacing:.5px;text-decoration:none}

/* contact */
.contact{left:0;top:3058px;width:1200px;height:443px;background:linear-gradient(180deg,#3b3e3c 0%,#2e332b 55%,#3a3f31 100%)}
.contact .section-title{position:absolute;left:0;top:58px;width:1200px;text-align:center;color:var(--white)}
.field{position:absolute;background:var(--white);font-family:Montserrat,sans-serif;font-weight:700;font-size:13px;color:var(--ink);padding:0 14px;display:flex;align-items:center;letter-spacing:.3px}
.field.msg{align-items:flex-start;padding-top:18px}

/* footer */
.footer{left:0;top:3501px;width:1200px;height:207px;background:var(--footer)}
.footer-nav{position:absolute;top:52px;left:0;width:1200px;display:flex;justify-content:center;gap:50px}
.footer-nav a{font-family:Montserrat,sans-serif;font-weight:700;font-size:14px;color:var(--white);text-decoration:none;letter-spacing:.3px}
.copy{position:absolute;top:93px;left:0;width:1200px;text-align:center;font-size:14px;color:var(--white)}
.social-foot{position:absolute;top:126px;left:480px;display:flex;gap:26px}
.social-foot span{width:28px;height:28px;border-radius:50%;border:3px solid var(--white)}
</style>
</head>
<body>

<!-- hero -->
<div class="photo hero" role="img" aria-label="Modern brick and concrete mixed-use development with arched ground floor, lawn and landscaped gardens"></div>
<div class="abs hero-shade"></div>
<nav class="nav">
  <a class="active" href="#">HOME</a>
  <a href="#" style="left:166px">PROPERTY</a>
  <a href="#" style="left:274px">CAPITAL &amp; FINANCE</a>
  <a href="#" style="left:804px">ABOUT</a>
  <a href="#" style="left:891px">CONTACT</a>
</nav>
<div class="abs brand">PELORIS</div>
<div class="abs social-top"><span></span><span></span><span></span><span></span><span></span></div>
<h1 class="abs hero-title">PELORIS</h1>
<p class="abs hero-sub">Property group that does property acquisitions, property development and property management.</p>
<div class="abs dots"><span class="on"></span><span></span><span></span><span></span></div>

<!-- intro -->
<p class="abs intro">Lorem ipsum dolor sit amet, consectetur adipiscing elit. Quisque nec odio nulla.<br>Quisque eleifend, lacus non aliquam porttitor, felis orci lobortis dolor,<br>non sollicitudin quam risus sed nisi</p>

<!-- property -->
<section class="abs property">
  <h2 class="section-title">PROPERTY</h2>
</section>

<div class="photo card-photo" style="left:75px;top:1015px;background:linear-gradient(135deg,#9a9c98,#e4e4e0 55%,#b9bcb6)" role="img" aria-label="Hands signing a lease document beside a set of keys"></div>
<div class="abs card" style="left:86px;top:1238px">
  <h3>LEASING</h3>
  <p>Aliquam accumsan auctor est eu laoreet sapien a felis efficitur laoreet eget ac nunc. Integer tristique turpis ut scelerisque ullamcorper.</p>
  <a href="#">READ MORE</a>
</div>

<div class="photo card-photo" style="left:614px;top:1015px;background:linear-gradient(180deg,#8fb0d4 0%,#c9d8e6 45%,#5a4a3e 80%,#6d7a58 100%)" role="img" aria-label="Dark brick apartment building against a blue sky"></div>
<div class="abs card" style="left:626px;top:1238px">
  <h3>PROJECTS</h3>
  <p>Aliquam accumsan auctor est eu laoreet sapien a felis efficitur laoreet eget ac nunc. Integer tristique turpis ut scelerisque ullamcorper.</p>
  <a href="#">READ MORE</a>
</div>

<div class="photo card-photo" style="left:75px;top:1481px;background:linear-gradient(135deg,#5c5650,#d9d6d0 50%,#4a4e58)" role="img" aria-label="Three business people meeting at a bright office table"></div>
<div class="abs card" style="left:86px;top:1704px">
  <h3>INVESTMENTS</h3>
  <p>Aliquam accumsan auctor est eu laoreet sapien a felis efficitur laoreet eget ac nunc. Integer tristique turpis ut scelerisque ullamcorper.</p>
  <a href="#">READ MORE</a>
</div>

<div class="photo card-photo" style="left:614px;top:1481px;background:linear-gradient(135deg,#b8bcc4,#eceae6 45%,#c0614a 70%,#8a8f98)" role="img" aria-label="Scale model of a red apartment building on a desk with charts"></div>
<div class="abs card" style="left:626px;top:1704px">
  <h3>PROPERTY MANAGEMENT</h3>
  <p>Aliquam accumsan auctor est eu laoreet sapien a felis efficitur laoreet eget ac nunc. Integer tristique turpis ut scelerisque ullamcorper.</p>
  <a href="#">READ MORE</a>
</div>

<!-- about -->
<div class="photo" style="left:0;top:2055px;width:600px;height:466px;background:linear-gradient(135deg,#c9d6e6,#e6e8ea 50%,#9aa08a 80%,#c98a6a)" role="img" aria-label="Two agents reviewing a scale model of a housing estate"></div>
<div class="abs split" style="left:652px;top:2125px;width:475px">
  <h2 class="section-title">ABOUT US</h2>
  <p>Aliquam accumsan auctor est eu laoreet. Quisque ut sapien a felis efficitur laoreet eget ac nunc. Integer tristique turpis ut scelerisque ullamcorper. Donec semper et nisl at luctus. Morbi rutrum tellus et varius pellentesque. Suspendisse vitae nulla id libero pulvinar euismod. Cras ipsum ligula, posuere eu venenatis eget, mollis vel ipsum auctor est eu laoreet.</p>
</div>
<a class="abs btn" href="#" style="left:652px;top:2390px">READ MORE</a>

<!-- capital & finance -->
<div class="abs split" style="left:76px;top:2592px;width:475px">
  <h2 class="section-title">CAPITAL &amp; FINANCE</h2>
  <p>Aliquam accumsan auctor est eu laoreet. Quisque ut sapien a felis efficitur laoreet eget ac nunc. Integer tristique turpis ut scelerisque ullamcorper. Donec semper et nisl at luctus. Morbi rutrum tellus et varius pellentesque. Suspendisse vitae nulla id libero pulvinar euismod. Cras ipsum ligula, posuere eu venenatis eget, mollis vel ipsum auctor est eu laoreet.</p>
</div>
<a class="abs btn" href="#" style="left:76px;top:2856px">READ MORE</a>
<div class="photo" style="left:600px;top:2521px;width:600px;height:466px;background:linear-gradient(135deg,#7a6452,#d8dde4 45%,#eef0f2 65%,#2e3440)" role="img" aria-label="Hands working with a calculator, financial reports and a laptop"></div>

<!-- contact -->
<section class="abs contact" role="img" aria-label="Darkened view of a brick development with arched windows">
  <h2 class="section-title">CONTACT US</h2>
</section>
<div class="field" style="left:253px;top:3193px;width:334px;height:49px">NAME</div>
<div class="field" style="left:253px;top:3255px;width:334px;height:49px">EMAIL ADDRESS</div>
<div class="field" style="left:253px;top:3316px;width:334px;height:48px">PHONE NO</div>
<div class="field msg" style="left:613px;top:3193px;width:332px;height:171px">MESSAGE</div>
<a class="abs btn" href="#" style="left:498px;top:3382px">READ MORE</a>

<!-- footer -->
<footer class="abs footer">
  <nav class="footer-nav">
    <a href="#">HOME</a><a href="#">PROPERTY</a><a href="#">CAPITAL AND FINANCE</a><a href="#">ABOUT</a><a href="#">CONTACT</a>
  </nav>
  <p class="copy">Copyright &nbsp;©2019 CompanyName.All Rights Reserved.</p>
  <div class="social-foot"><span></span><span></span><span></span><span></span><span></span></div>
</footer>

</body>
</html>
```